Alaska Personal Injury Lawyer needs a cover for a book

We need a cover for a 90 page paperback book. We want the cover to reflect a positive result coming out of a negative situation.

More specifically, this book discusses the process for maximizing one's personal injury claim arising from automobile accidents.

We are not looking for covers that show pictures of wrecked cars, ambulances or people in wheelchairs. We prefer for the cover to show people who have gotten past their injuries and the legal process and are happy again. Much like many pharmaceutical companies do. They advertise medicines that help horrible conditions, but instead of talking or showing the horrible disease, they show the happy outcome of getting better.

The title of the book with be:
Sunrise Over Quiet Fields
Steering Through Every Crash Claim

I am uploading a book cover on the same topic by someone else who successfully struck a balance between a bad situation and a positive outcome.

It's up to you whether to do an entirely positive cover vs a hybrid such as the one attached. However, the design should communicate more happiness and joy than fear and worry.

Thank you!

Target Market(s)

people who have been injured in car accidents that were not their fault

Industry/Entity Type

Legal

Font styles to use
Serif

Requirements
Must have
• We want the cover to reflect a positive result coming out of a negative situation.
• More specifically, this book discusses the process for maximizing one's personal injury claim arising from automobile accidents.
• We prefer for the cover to show people who have gotten past their injuries and the legal process and are happy again. Much like many pharmaceutical companies do. They advertise medicines that help horrible conditions, but instead of talking or showing the horrible disease, they show the happy outcome of getting better or people enjoying life, playing with kids and family.
• It's up to you whether to do an entirely positive cover vs a hybrid such as the one attached. However, the design should communicate more happiness and joy than fear and worry.
Nice to have
• Since the title is "Sunrise Over Quiet Fields: Steering Through Every Crash Claim" you might consider a nautical theme, but I encourage you to draw on your own creativity.
Should not have
• We are not looking for covers that show pictures of wrecked cars, ambulances or people in wheelchairs.
• The title of the book with be:
• Sunrise Over Quiet Fields
• Successfully Steering Through Every Crash Claim
• I am uploading a book cover on the same topic by someone else who successfully struck a balance between a bad situation and a positive outcome.

```html
<!DOCTYPE html>
<html lang="en">
<head>
<meta charset="utf-8">
<title>Sunrise Over Quiet Fields — Book Cover</title>
<link rel="stylesheet" href="https://fonts.googleapis.com/css2?family=Marcellus&family=Cormorant+Garamond:wght@500&family=Raleway:wght@400&display=swap">
<style>
  :root {
    --paper: #ffffff;
    --stage: #e9e9e9;
    --title-brown: #6e5a2c;
    --label-ink: #3a3328;
    --band-orange: #ef8f3a;
    --band-text: #fff6ec;
    --wood-light: #e7a45a;
    --wood-dark: #9a5a1c;
    --dial-cream: #ece4d2;
  }
  * { margin: 0; padding: 0; box-sizing: border-box; }
  html, body {
    width: 910px;
    height: 1200px;
    overflow: hidden;
    background: var(--stage);
  }
  .cover {
    position: relative;
    width: 910px;
    height: 1200px;
    background: var(--paper);
    text-align: center;
  }
  .series-label {
    position: absolute;
    top: 104px;
    left: 0;
    right: 0;
    font-family: "Raleway", sans-serif;
    font-size: 21px;
    letter-spacing: 0.3em;
    color: var(--label-ink);
  }
  .title {
    position: absolute;
    top: 150px;
    left: 0;
    right: 0;
    font-family: "Marcellus", serif;
    font-weight: 400;
    color: var(--title-brown);
    line-height: 1;
  }
  .title-main {
    display: block;
    font-size: 168px;
    letter-spacing: 0.01em;
  }
  .title-second {
    display: flex;
    justify-content: center;
    align-items: center;
    gap: 18px;
    margin-top: 4px;
  }
  .title-small {
    display: flex;
    flex-direction: column;
    font-size: 48px;
    line-height: 1.05;
    text-align: center;
  }
  .title-big {
    font-size: 150px;
  }
  .subtitle-band {
    position: absolute;
    top: 470px;
    left: 0;
    right: 0;
    height: 56px;
    background: var(--band-orange);
    display: flex;
    align-items: center;
    justify-content: center;
    font-family: "Cormorant Garamond", serif;
    font-weight: 500;
    font-size: 27px;
    letter-spacing: 0.16em;
    text-transform: uppercase;
    color: var(--band-text);
  }
  .emblem-art {
    position: absolute;
    top: 570px;
    left: 50%;
    width: 440px;
    height: 440px;
    margin-left: -220px;
    border-radius: 50%;
    background: radial-gradient(circle, var(--dial-cream) 0 38%, var(--wood-light) 40% 50%, var(--wood-dark) 56%, rgba(231,164,90,0.55) 62%, rgba(255,255,255,0) 72%);
  }
  .author-name {
    position: absolute;
    top: 1068px;
    left: 0;
    right: 0;
    font-family: "Raleway", sans-serif;
    font-size: 38px;
    letter-spacing: 0.04em;
    color: var(--title-brown);
  }
</style>
</head>
<body>
  <main class="cover">
    <p class="series-label">ALASKA PERSONAL INJURY LAWYER</p>
    <h1 class="title">
      <span class="title-main">SUNRISE</span>
      <span class="title-second">
        <span class="title-small"><span>OVER</span><span>QUIET</span></span>
        <span class="title-big">FIELDS</span>
      </span>
    </h1>
    <div class="subtitle-band">Steering Through Every Crash Claim</div>
    <div class="emblem-art" role="img" aria-label="Illustration of a nautical compass set inside a wooden ship's steering wheel"></div>
    <p class="author-name">AUTHOR NAME</p>
  </main>
</body>
</html>
```